BRELTONAllies.co.uk - Mental Health Clinic for Child and Adolescents

Updated 29/01/2018***
I am not sure you guys are getting the idea regards to the opening page / homescreen layout. Can you look at the new images I have uploaded (page 5, 6 and 7) These are some of the layouts I like but to incorporate my chosen images, with the CAMHS commissioner, buttons and a sliding header bar.
I have written a strong brief, I am looking for a website, preferably wordpress as i know they are easy to maintain. I am looking for a one page site, with the top / opening page being full screen image with drop down categories. I have made a rough design, see full brief in word doc attached, there is some freedom to play around with the design aspect but it will need to relay all the content provided. I like a minimal feel. I have also attached some images that may be useful, but will need a new logo for BRELTON Allies. I have attached some logo idea's, it is up to you decide whether you want to use them.
I would prefer the homepage as full screen image, and the categories offered as a drop down or over the main image.
I have also attached linked to some competitors websites:
https://www.vorrendale-group.co.uk/
http://www.qmvd.org.uk/
Industry/Entity Type
Clinic
Number of Pages Required
1 page
Font styles to use
Look and feel
Each slider illustrates characteristics of the customer's brand and the style your logo design should communicate.

```html
<!DOCTYPE html>
<html lang="en">
<head>
<meta charset="utf-8">
<title>BRELTON Allies – Parents and Commissioners</title>
<link rel="stylesheet" href="https://fonts.googleapis.com/css2?family=Open+Sans:ital,wght@0,300;0,400;0,600;0,700;1,400&family=Carlito:ital,wght@0,400;0,700;1,400;1,700&display=swap">
<style>
  :root {
    --ink: #1f2a33;
    --body: #2b2b2b;
    --link: #1c1f9c;
    --accent: #30e3ee;
    --accent-text: #24d0e6;
    --rail: #2c3844;
    --paper: #ffffff;
  }
  * { margin: 0; padding: 0; box-sizing: border-box; }
  html, body { width: 1200px; height: 1200px; overflow: hidden; background: var(--paper); }
  body { position: relative; font-family: "Open Sans", Arial, sans-serif; color: var(--body); }

  .rail { position: absolute; left: 0; top: 0; width: 4px; height: 1200px; background: var(--rail); }

  .photo { position: absolute; }
  .photo--parents {
    left: 4px; top: 0; width: 604px; height: 561px;
    background:
      linear-gradient(90deg, rgba(255,255,255,0) 0%, rgba(255,255,255,0) 55%, rgba(255,255,255,0.85) 85%, #fff 100%),
      linear-gradient(100deg, #4b4d4f 0%, #6c6a68 22%, #d9dadb 40%, #e6e4e2 60%, #b9b6b3 75%, #eeeeee 100%);
  }
  .photo--commissioners {
    left: 520px; top: 568px; width: 680px; height: 525px;
    background:
      linear-gradient(90deg, #fff 0%, rgba(255,255,255,0.85) 12%, rgba(255,255,255,0) 35%),
      linear-gradient(90deg, rgba(255,255,255,0) 0%, rgba(255,255,255,0) 60%, rgba(44,42,60,0.5) 100%),
      radial-gradient(ellipse at 70% 45%, #e9b993 0%, #c98f6e 30%, rgba(201,143,110,0) 60%),
      linear-gradient(180deg, #f2d2ad 0%, #b58a6c 45%, #e8e6e6 75%, #cfd3da 100%);
  }

  .section-title {
    position: absolute; font-weight: 400; font-size: 29px; color: var(--ink);
    letter-spacing: 0.5px; line-height: 1;
  }
  .parents .section-title { left: 594px; top: 56px; }
  .commissioners .section-title { left: 84px; top: 638px; }

  .lead { position: absolute; font-size: 18.2px; line-height: 28.8px; color: var(--body); }
  .lead .line { display: block; white-space: nowrap; }
  .parents .lead { left: 598px; top: 99px; }
  .commissioners .lead { left: 90px; top: 690px; width: 533px; }
  .commissioners .lead .line { text-align: justify; text-align-last: justify; }
  .commissioners .lead .line--last { text-align-last: left; }

  .note { position: absolute; font-family: "Carlito", Calibri, sans-serif; font-style: italic; font-size: 20.5px; line-height: 24px; color: #222; }
  .note .line { display: block; white-space: nowrap; }
  .parents .note { left: 598px; top: 318px; }
  .commissioners .note { left: 90px; top: 894px; font-weight: 700; font-size: 21px; }
  .note .call { color: var(--link); }

  .offer { position: absolute; left: 596px; top: 448px; }
  .offer h3 { font-size: 18.2px; font-weight: 700; color: #111; line-height: 24px; }
  .offer ul { list-style: none; margin-top: 5px; }
  .offer li { position: relative; padding-left: 38px; font-size: 18.2px; font-weight: 700; line-height: 29px; }
  .offer li::before { content: ""; position: absolute; left: 2px; top: 13px; width: 5px; height: 5px; border-radius: 50%; background: #111; }
  .offer a { color: var(--link); text-decoration: underline; }

  .btn-contact {
    position: absolute; left: 82px; top: 982px; width: 250px; height: 55px;
    border-radius: 28px; background: var(--accent); color: #fff;
    font-weight: 700; font-size: 20.5px; letter-spacing: 0.3px;
    display: flex; align-items: center; justify-content: center; text-decoration: none;
  }

  .services-title {
    position: absolute; left: 0; top: 1162px; width: 1200px; text-align: center;
    font-size: 29px; font-weight: 400; color: var(--ink); letter-spacing: 0.5px; line-height: 1;
  }
  .services-title span { color: var(--accent-text); }
</style>
</head>
<body>
  <div class="rail"></div>

  <section class="parents">
    <div class="photo photo--parents" role="img" aria-label="Photo of a boy in a grey hoodie sitting at a desk talking with a clinician"></div>
    <h2 class="section-title">PARENTS</h2>
    <p class="lead">
      <span class="line">Are you looking for a thorough, efficient, highly accurate</span>
      <span class="line">screening or assessment for your child?&nbsp; We use both elec-</span>
      <span class="line">tronic and paper based screening tools so that we can be</span>
      <span class="line">flexible to what works better around you. We will deliver</span>
      <span class="line">you the results within 24 hours after our screening tools</span>
      <span class="line">have been completed, and will make recommendations</span>
      <span class="line">based around these results.</span>
    </p>
    <p class="note">
      <span class="line">Should you opt to have a full ADHD / ASD assessment we aim to</span>
      <span class="line">have appointments available with 14 days.&nbsp; All of our clinicians</span>
      <span class="line">have been specifically chosen as they are some of the best in</span>
      <span class="line">their specialist field.</span>
    </p>
    <div class="offer">
      <h3>We offer the following assessments:</h3>
      <ul>
        <li><a href="#">OBSA</a></li>
        <li><a href="#">DPI-R</a></li>
      </ul>
    </div>
  </section>

  <section class="commissioners">
    <div class="photo photo--commissioners" role="img" aria-label="Photo of two people shaking hands over a desk with charts and a pen"></div>
    <h2 class="section-title">COMMISSIONERS</h2>
    <p class="lead">
      <span class="line">Are you looking to reduce waiting times or commission part</span>
      <span class="line">of your ADHD or ASD pathway?&nbsp; We have a proven track</span>
      <span class="line">record in providing robust, high quality, patient focused as-</span>
      <span class="line">sessment and post-assessment treatment.&nbsp; We can come</span>
      <span class="line">take referrals at a variety of stages and are able to offer the</span>
      <span class="line line--last">highest levels of service and exceptional value.</span>
    </p>
    <p class="note">
      <span class="line"><span class="call">CALL US</span> today to discuss how we can be supporting part of</span>
      <span class="line">your service.</span>
    </p>
    <a class="btn-contact" href="#">CONTACT US!</a>
  </section>

  <h2 class="services-title">OUR <span>SERVICES</span></h2>
</body>
</html>
```